Combining web page

We need a PSD webpage design for our PrestaShop store that shows food combining rules, you can see an example that we put here, you can follow the same information and food image combinations. You are just doing the design but the images when implemented on the website will be clickable that goes to product categories, all text and images will be editable.

This is just an example:
http://merrowtonic.com/content/7-food-combining-rules

Target Market(s)

Natural Product and supplement industry

Industry/Entity Type

Store

Number of Pages Required

1 page

Colors

Designer to choose colors to be used in the design.

Requirements
Must have
• 1. Clear images.
• 2. Clear readable text.
• 3. Company name shown Merrow Tonic.
• 4. Follow the food rules as seen on the web page example, but not the same design.
• 5. Logo should be seen.
• 7. All text and images will be editable.
• 8. Make sure the food images are in their proper groups.
• 9. You are not coping the design we gave you but the details have to be the same, copy the text and the image food groups are important, you cannot just put any food in a group, and the combinations are important.
Nice to have
• Here is the website it is for http://merrowtonic.com/

```html
<!DOCTYPE html>
<html lang="en">
<head>
<meta charset="utf-8">
<title>Merrow Tonic – Food Combining Made Easy</title>
<link href="https://fonts.googleapis.com/css2?family=Barlow+Semi+Condensed:wght@500;600;700&display=swap" rel="stylesheet">
<style>
  :root {
    --page: #f1ede0;
    --header: #ffffff;
    --nav-text: #b0651e;
    --green: #8cc63f;
    --green-dark: #5fa32a;
    --yellow: #f2d03b;
    --ink: #1d1d1d;
    --white: #ffffff;
  }
  * { margin: 0; padding: 0; box-sizing: border-box; }
  html, body { width: 1200px; height: 797px; overflow: hidden; }
  body {
    font-family: "Barlow Semi Condensed", "Arial Narrow", sans-serif;
    background: var(--page);
    color: var(--ink);
    position: relative;
  }

  /* Header */
  .site-header {
    position: absolute; inset: 0 0 auto 0; height: 130px;
    background: var(--header);
  }
  .utility {
    position: absolute; top: 16px; right: 34px;
    display: flex; flex-direction: column; align-items: flex-end; gap: 10px;
    font-size: 13px; font-weight: 600;
  }
  .utility .login { color: var(--green); letter-spacing: .5px; }
  .utility .tools { display: flex; align-items: center; gap: 6px; color: #8a8a8a; font-size: 11px; }
  .tool-icon {
    width: 18px; height: 18px; border-radius: 50%; background: var(--green-dark);
    display: grid; place-items: center;
  }
  .brand {
    position: absolute; top: 22px; left: 50%; transform: translateX(-50%);
    text-align: center; white-space: nowrap;
  }
  .brand .tagline {
    font-size: 12px; font-weight: 700; color: var(--green); letter-spacing: .4px;
  }
  .brand .name {
    margin-top: 6px; display: flex; align-items: center; justify-content: center; gap: 8px;
    font-size: 30px; font-weight: 700; color: var(--green-dark);
  }
  .brand .mark { width: 16px; height: 16px; border-radius: 50%; background: var(--green-dark); }
  .main-nav {
    position: absolute; top: 96px; left: 0; right: 0;
    display: flex; justify-content: center;
    font-size: 15px; font-weight: 700; color: var(--nav-text); letter-spacing: .4px;
  }
  .main-nav .group { display: flex; align-items: center; }
  .main-nav .group.left { margin-right: 230px; }
  .main-nav a { color: inherit; text-decoration: none; }
  .main-nav .sep { color: var(--green); margin: 0 14px; font-weight: 500; }

  /* Food wheel */
  .food-wheel { position: absolute; inset: 130px 0 0 0; }
  .hero-circle {
    position: absolute; left: 470px; top: 200px; width: 290px; height: 290px;
    border-radius: 50%; background: var(--yellow); color: var(--white);
    display: flex; flex-direction: column; align-items: center; justify-content: center;
    text-align: center;
  }
  .hero-circle .count { font-size: 120px; font-weight: 700; line-height: .85; }
  .hero-circle .title { font-size: 26px; font-weight: 600; line-height: 1.1; letter-spacing: .5px; margin-top: 12px; }

  .food-group { position: absolute; display: flex; flex-direction: column; align-items: center; text-align: center; }
  .food-photo { width: 130px; height: 95px; border-radius: 46% 54% 48% 52%; }
  .badge {
    margin-top: 8px; width: 24px; height: 24px; border-radius: 50%;
    background: var(--ink); color: var(--white);
    font-size: 13px; font-weight: 700; display: grid; place-items: center;
  }
  .label { margin-top: 6px; font-size: 13px; font-weight: 600; line-height: 1.15; letter-spacing: .3px; white-space: nowrap; }

  .g-sub-acid   { left: 330px; top: 470px; }
  .g-sweet      { left: 150px; top: 330px; }
  .g-nuts       { left: 210px; top: 110px; }
  .g-grains     { left: 420px; top: 14px; }
  .g-legumes    { left: 690px; top: 14px; }
  .g-melons     { left: 850px; top: 110px; }
  .g-vegetables { left: 930px; top: 270px; }

  .ph-sub-acid   { background: linear-gradient(135deg, #f59b2b, #e94b3c 55%, #9cc24a); }
  .ph-sweet      { background: linear-gradient(135deg, #7a9a3a, #f3c63a 50%, #e9d9a8); }
  .ph-nuts       { background: linear-gradient(135deg, #f2b81e, #8a5a2b 55%, #6f9a34); }
  .ph-grains     { background: linear-gradient(135deg, #c9a674, #8c6a45 55%, #e8dcc0); }
  .ph-legumes    { background: linear-gradient(135deg, #7dbb3c, #b6d88a 60%, #e8e2c6); }
  .ph-melons     { background: linear-gradient(135deg, #e86a4c, #f2d36a 50%, #8dbb4e); }
  .ph-vegetables { background: linear-gradient(135deg, #4e9a36, #f07a24 50%, #a0224e); }

  .cta {
    position: absolute; left: 700px; top: 520px;
    padding: 14px 34px; border-radius: 30px;
    background: var(--green); color: var(--white);
    font-size: 17px; font-weight: 700; letter-spacing: .6px; text-decoration: none;
  }
</style>
</head>
<body>
  <header class="site-header">
    <div class="utility">
      <span class="login">LOGIN</span>
      <div class="tools">
        <span class="tool-icon">
          <svg width="10" height="10" viewBox="0 0 10 10"><circle cx="4" cy="4" r="2.8" fill="none" stroke="#fff" stroke-width="1.4"/><line x1="6" y1="6" x2="9" y2="9" stroke="#fff" stroke-width="1.4"/></svg>
        </span>
        <span class="tool-icon">
          <svg width="10" height="10" viewBox="0 0 10 10"><path d="M1 2h1.5l1.2 5h4.3l1-3.5H3" fill="none" stroke="#fff" stroke-width="1.2"/></svg>
        </span>
        <span>(0 CART)</span>
      </div>
    </div>

    <div class="brand">
      <div class="tagline">TIMELESS FOODS FOR MODERN LIVING</div>
      <div class="name"><span class="mark"></span>Merrow Tonic</div>
    </div>

    <nav class="main-nav">
      <div class="group left">
        <a href="#">OUR PRODUCTS</a><span class="sep">|</span><a href="#">INGREDIENTS</a><span class="sep">|</span>
      </div>
      <div class="group right">
        <span class="sep">|</span><a href="#">HEALTH CONCERNS</a><span class="sep">|</span><a href="#">OUR BLOGS</a><span class="sep">|</span><a href="#">MORE</a>
      </div>
    </nav>
  </header>

  <main class="food-wheel">
    <div class="hero-circle">
      <span class="count">9</span>
      <span class="title">FOOD COMBINING<br>MADE EASY</span>
    </div>

    <div class="food-group g-sub-acid">
      <div class="food-photo ph-sub-acid" role="img" aria-label="Oranges, strawberries, apples and grapes"></div>
      <span class="badge">1</span>
      <span class="label">FRUITS SUB ACID</span>
    </div>

    <div class="food-group g-sweet">
      <div class="food-photo ph-sweet" role="img" aria-label="Pineapple, bananas and coconut"></div>
      <span class="badge">2</span>
      <span class="label">SWEET FRUITS<br>PALM FRUITS</span>
    </div>

    <div class="food-group g-nuts">
      <div class="food-photo ph-nuts" role="img" aria-label="Sunflower, mixed nuts and avocado"></div>
      <span class="badge">3</span>
      <span class="label">NATURAL FRUITS<br>RAW NUTS<br>SEEDS</span>
    </div>

    <div class="food-group g-grains">
      <div class="food-photo ph-grains" role="img" aria-label="Sacks and bowls of grains and corn"></div>
      <span class="badge">4</span>
      <span class="label">GRAINS</span>
    </div>

    <div class="food-group g-legumes">
      <div class="food-photo ph-legumes" role="img" aria-label="Pea pods and fresh sprouts"></div>
      <span class="badge">5</span>
      <span class="label">LEGUMES<br>SPROUTS</span>
    </div>

    <div class="food-group g-melons">
      <div class="food-photo ph-melons" role="img" aria-label="Sliced watermelon and assorted melons"></div>
      <span class="badge">6</span>
      <span class="label">MELONS</span>
    </div>

    <div class="food-group g-vegetables">
      <div class="food-photo ph-vegetables" role="img" aria-label="Carrots, cabbage, beetroot and leafy greens"></div>
      <span class="badge">8</span>
      <span class="label">VEGETABLES<br>LEAFY, FLOWER, ROOTS</span>
    </div>

    <a class="cta" href="#">EXPLORE FOOD TABLE</a>
  </main>
</body>
</html>
```